Looking for copywriting of the entire website + new selection of pictures

Hello,
My website's copy write is on the weaker side, so I'm looking for an entire re-do of my website's copy write. If you think a line is weak, re-write, otherwise you can leave it as is. We want our site to clearly explain what our events are, how they work, and why someone should sign up for them, while appealing to the hopeful, romantic, and nostalgic feelings of the visitors. Our speed dating events can be imagined as a modern day approach to the old-fashioned way of dating, where people got to know each other in person, away from the dating apps!! Additionally, I feel nearly all the existing pictures are rather weak, so please select entirely new pictures which give the website a less amateur feel, while retaining the playful nature of the brand. If there are areas where you think that section would benefit from no pictures at all, please communicate that.
Let me know if there are any further questions and thank you!
You can find the site at:
https://www.lanternmeetups.com
Industry/Entity Type
Speed Dating/Romance
Number of Pages Required
1 page
Look and feel
Each slider illustrates characteristics of the customer's brand and the style your logo design should communicate.

```html
<!DOCTYPE html>
<html lang="en">
<head>
<meta charset="utf-8">
<title>Lantern Meetups</title>
<link rel="stylesheet" href="https://fonts.googleapis.com/css2?family=Outfit:wght@400;500;600&family=Inter:wght@400;500;600;700&display=swap">
<style>
:root{
  --stage:#231418;
  --pink:#ffcadd;
  --pink-soft:#fde6ee;
  --grey:#e8e8e8;
  --black:#000000;
  --white:#ffffff;
  --ink:#111111;
  --heart:#e0344a;
  --rule:#6b6b6b;
}
*{box-sizing:border-box;margin:0;padding:0}
html,body{width:1200px;height:4165px;overflow:hidden;background:var(--stage)}
body{font-family:"Inter",sans-serif;color:var(--ink);position:relative}
.page{position:absolute;left:60px;top:7px;width:1080px;height:4151px;border-radius:20px;overflow:hidden;background:var(--white)}
.section{position:absolute;left:0;width:1080px}
.abs{position:absolute}
h1,h2,h3{font-family:"Outfit",sans-serif;font-weight:500;letter-spacing:-0.3px}
.brand-name{font-family:"Inter",sans-serif;font-weight:700;font-size:15px;color:var(--ink);display:flex;align-items:center;gap:6px;white-space:nowrap}
.brand-name .dot{width:10px;height:10px;border-radius:50%;background:var(--ink)}
.btn{position:absolute;display:flex;align-items:center;justify-content:center;border-radius:20px;font-size:9px;font-weight:600;letter-spacing:.4px;text-transform:uppercase}
.btn-dark{background:var(--black);color:var(--white)}
.btn-outline{border:1.5px solid var(--black);color:var(--ink);background:transparent}

/* nav */
.nav{top:0;height:111px;background:var(--pink)}
.nav-link{position:absolute;top:46px;font-size:12px}
.nav .brand-name{position:absolute;left:540px;top:45px;transform:translateX(-50%)}
.social{position:absolute;top:47px;font-size:10px;font-weight:600}
.nav .btn{left:960px;top:40px;width:90px;height:30px;font-size:9px;text-transform:none;letter-spacing:0}

/* hero */
.hero{top:111px;height:416px;background:var(--pink-soft)}
.hero-photo{position:absolute;left:380px;top:0;width:700px;height:416px;background:linear-gradient(90deg,rgba(253,230,238,1) 0%,rgba(245,220,222,.8) 25%,#e6cfc9 50%,#cdb7ad 75%,#b99f93 100%)}
.eyebrow{left:137px;top:105px;font-size:12px;font-weight:700}
.hero h1{position:absolute;left:137px;top:128px;font-size:39px}
.hero p{position:absolute;left:137px;top:188px;width:340px;font-size:10.5px;line-height:17px}

/* locations */
.locations{top:527px;height:233px;background:var(--pink)}
.locations h2{position:absolute;left:137px;top:92px;font-size:38px}
.pin-pill{position:absolute;height:40px;width:196px;border:1.5px solid var(--black);background:var(--white);border-radius:10px;display:flex;align-items:center;padding-left:18px;gap:24px;font-size:11.5px;text-decoration:underline}
.pin-pill svg{width:20px;height:22px;flex:none}

/* newsletter */
.newsletter{top:760px;height:461px;background:var(--grey)}
.pattern{position:absolute;inset:0;background:linear-gradient(135deg,#ececec,#e3dfe0)}
.news-card{position:absolute;left:137px;top:123px;width:806px;height:212px;background:var(--black);border-radius:10px;color:var(--white);text-align:center}
.news-card h2{margin-top:38px;font-size:37px;font-weight:400}
.news-card p{margin-top:18px;font-size:11.5px;font-weight:600}
.news-card .btn{left:345px;top:138px;width:116px;height:32px;background:var(--pink);color:var(--ink);font-size:8.5px}

/* coffee */
.coffee{top:1221px;height:384px;background:var(--pink)}
.coffee-photo{position:absolute;left:137px;top:34px;width:320px;height:316px;border-radius:16px;background:linear-gradient(150deg,#3a2e29 0%,#6a5c54 45%,#2b2220 75%,#8a1c22 100%)}
.tag{position:absolute;left:501px;top:88px;background:var(--white);border-radius:4px;padding:2px 7px;font-size:11px;font-weight:600}
.coffee h2{position:absolute;left:501px;top:118px;font-size:40px}
.coffee p{position:absolute;left:501px;top:180px;width:470px;font-size:11px;line-height:19px}
.coffee .btn{left:501px;top:282px;width:122px;height:34px}

/* how */
.how{top:1605px;height:523px;background:var(--grey)}
.how h2{position:absolute;left:137px;top:130px;font-size:38px}
.how-intro{position:absolute;left:137px;top:185px;font-size:10.5px;line-height:15px}
.step{position:absolute;left:130px;height:38px;background:var(--white);border-radius:10px;display:flex;align-items:center;gap:8px;padding:0 14px;font-size:10.5px}
.step svg{width:11px;height:11px}
.how-photo{position:absolute;left:544px;top:106px;width:399px;height:336px;border-radius:16px;background:radial-gradient(circle at 35% 30%,#d8d4d6 0%,#5a4a4d 25%,#231a1c 60%,#100c0d 100%)}

/* rounds */
.rounds{top:2128px;height:247px;background:var(--black);color:var(--white)}
.rounds p{position:absolute;left:0;width:1080px;top:64px;text-align:center;font-size:11px;line-height:19px}
.rounds p strong{color:var(--pink);font-weight:600}
.round-box{position:absolute;top:119px;width:264px;height:66px;background:var(--pink);border-radius:8px;color:var(--ink);display:flex;align-items:center;justify-content:center;font-size:11.5px;font-weight:600}

/* casual */
.casual{top:2375px;height:542px;background:var(--pink)}
.casual h2{position:absolute;left:0;width:1080px;top:50px;text-align:center;font-size:42px}
.code-card{position:absolute;top:137px;width:264px;height:363px;background:var(--white);border:1.5px solid var(--ink);border-radius:10px;padding:26px 34px}
.code-card svg{width:40px;height:40px}
.code-card h3{margin-top:8px;font-size:25px;line-height:31px;font-weight:400}
.code-card p{margin-top:30px;font-size:9.5px;line-height:16px}

/* faq */
.faq{top:2917px;height:963px;background:var(--grey)}
.faq h2{position:absolute;left:0;width:1080px;top:88px;text-align:center;font-size:38px}
.faq-list{position:absolute;left:137px;top:180px;width:806px;list-style:none;border-top:1.5px solid var(--rule)}
.faq-list li{height:57.6px;border-bottom:1.5px solid var(--rule);display:flex;align-items:center;justify-content:space-between;font-size:12.5px}
.faq-list li span:last-child{font-size:16px}

/* footer */
.footer{top:3880px;height:271px;background:var(--white);text-align:center}
.footer .brand-name{position:absolute;left:540px;top:52px;transform:translateX(-50%)}
.footer h3{position:absolute;left:0;width:1080px;top:119px;font-family:"Inter",sans-serif;font-size:13px;font-weight:600}
.footer .line{position:absolute;left:0;width:1080px;font-size:9.5px}
</style>
</head>
<body>
<div class="page">

  <header class="section nav">
    <span class="nav-link" style="left:41px">Home</span>
    <span class="nav-link" style="left:109px">Event Locations</span>
    <span class="nav-link" style="left:237px">How it Works</span>
    <span class="nav-link" style="left:350px">FAQ</span>
    <div class="brand-name"><span class="dot"></span>Lantern Meetups</div>
    <span class="social" style="left:806px">Pixly</span>
    <span class="social" style="left:850px">Loopz</span>
    <span class="social" style="left:898px">Circlo</span>
    <span class="btn btn-dark">Contact Us</span>
  </header>

  <section class="section hero">
    <div class="hero-photo" role="img" aria-label="Couple walking hand in hand along a misty beach at sunset"></div>
    <span class="abs eyebrow">Stop swiping, Start Dating!</span>
    <h1>Lantern Meetups</h1>
    <p>Upgrade your dating vibe—no hosts, just fun convos. Dive into instant joy at our exciting events. Your match is ready to party!</p>
    <span class="btn btn-dark" style="left:137px;top:264px;width:122px;height:34px">How it works</span>
    <span class="btn btn-outline" style="left:270px;top:264px;width:112px;height:34px">Our events</span>
  </section>

  <section class="section locations">
    <h2>Event Locations</h2>
    <div class="pin-pill" style="left:510px;top:71px"><svg viewBox="0 0 20 22"><path d="M10 1a7 7 0 0 0-7 7c0 5 7 13 7 13s7-8 7-13a7 7 0 0 0-7-7z" fill="#000"/><circle cx="10" cy="8" r="2.6" fill="#fff"/></svg>BOSTON, MA</div>
    <div class="pin-pill" style="left:713px;top:71px"><svg viewBox="0 0 20 22"><path d="M10 1a7 7 0 0 0-7 7c0 5 7 13 7 13s7-8 7-13a7 7 0 0 0-7-7z" fill="#000"/><circle cx="10" cy="8" r="2.6" fill="#fff"/></svg>PHILADELPHIA, PA</div>
    <div class="pin-pill" style="left:543px;top:120px"><svg viewBox="0 0 20 22"><path d="M10 1a7 7 0 0 0-7 7c0 5 7 13 7 13s7-8 7-13a7 7 0 0 0-7-7z" fill="#000"/><circle cx="10" cy="8" r="2.6" fill="#fff"/></svg>JERSEY CITY, NJ</div>
    <div class="pin-pill" style="left:750px;top:120px"><svg viewBox="0 0 20 22"><path d="M10 1a7 7 0 0 0-7 7c0 5 7 13 7 13s7-8 7-13a7 7 0 0 0-7-7z" fill="#000"/><circle cx="10" cy="8" r="2.6" fill="#fff"/></svg>NEW YORK CITY, NY</div>
  </section>

  <section class="section newsletter">
    <div class="pattern" role="img" aria-label="Playful pattern of hand-drawn pink hearts"></div>
    <div class="news-card">
      <h2>Our Events Fill Up Fast. Don’t Miss Out.</h2>
      <p>Join our monthly newsletter to see all events for that month.</p>
      <span class="btn">Click to join</span>
    </div>
  </section>

  <section class="section coffee">
    <div class="coffee-photo" role="img" aria-label="Hands holding a coffee cup beside red roses on a café table"></div>
    <span class="tag">Lantern Meetups</span>
    <h2>Swift Coffee Connections</h2>
    <p>Tired of awkward intros? Try our Coffee Date Speed Meet! It’s as chill as a coffee hangout but with the potential for something more. Find an event nearby and dive into genuine connections. No clichés, just real conversations. Ready to spice up your dating game?</p>
    <span class="btn btn-dark">Get started</span>
  </section>

  <section class="section how">
    <h2>How It Goes</h2>
    <p class="how-intro">No hosts, no name tags – we keep it real simple.<br>Just show up at your time and place</p>
    <div class="step" style="top:243px"><svg viewBox="0 0 12 11"><path d="M6 10.5 1.2 5.6A2.8 2.8 0 0 1 6 2a2.8 2.8 0 0 1 4.8 3.6z" fill="#e0344a"/></svg>Get our texts with round times and who you’re meeting.</div>
    <div class="step" style="top:290px"><svg viewBox="0 0 12 11"><path d="M6 10.5 1.2 5.6A2.8 2.8 0 0 1 6 2a2.8 2.8 0 0 1 4.8 3.6z" fill="#e0344a"/></svg>Find your date, grab a seat, and chat away!</div>
    <div class="step" style="top:337px"><svg viewBox="0 0 12 11"><path d="M6 10.5 1.2 5.6A2.8 2.8 0 0 1 6 2a2.8 2.8 0 0 1 4.8 3.6z" fill="#e0344a"/></svg>Text us after each round: Match (M) or Pass (P).</div>
    <div class="step" style="top:385px"><svg viewBox="0 0 12 11"><path d="M6 10.5 1.2 5.6A2.8 2.8 0 0 1 6 2a2.8 2.8 0 0 1 4.8 3.6z" fill="#e0344a"/></svg>Keep the fun going – repeat and enjoy!</div>
    <div class="how-photo" role="img" aria-label="Couple sharing wine at a small bar table under a neon sign"></div>
  </section>

  <section class="section rounds">
    <p>Our events feature 7 rounds, each lasting 10 minutes. It provides ample time for genuine connections<br>and getting to know each other’s vibe. No scripted conversations – <strong>just real and interesting chats!</strong></p>
    <div class="round-box" style="left:137px">7 Rounds</div>
    <div class="round-box" style="left:408px">7 Dates</div>
    <div class="round-box" style="left:679px">7 Opportunities for something new</div>
  </section>

  <section class="section casual">
    <h2>Casual Is Our Code</h2>
    <div class="code-card" style="left:137px">
      <svg viewBox="0 0 40 40"><path d="M13 6 3 12l4 8 4-2v18h18V18l4 2 4-8-10-6c-1 3-3 5-7 5s-6-2-7-5z" fill="#000"/></svg>
      <h3>Casual<br>Dress</h3>
      <p>Feel free to wear whatever makes you feel at ease – whether it’s business casual or your favorite sweater. Your style reflects who you are, and that’s what matters to us. Our dates are laid-back with no expectations, so just show up and connect.</p>
    </div>
    <div class="code-card" style="left:408px">
      <svg viewBox="0 0 40 40"><path d="M22 4c8 0 14 5 14 12 0 6-5 11-12 12l-6 6v-7c-6-2-10-6-10-11 0-7 6-12 14-12z" fill="#000"/><circle cx="16" cy="16" r="2" fill="#fff"/><circle cx="22" cy="16" r="2" fill="#fff"/><circle cx="28" cy="16" r="2" fill="#fff"/></svg>
      <h3>Casual<br>Conversation</h3>
      <p>On multiple short dates, skip the formalities! Use our provided prompts for engaging and in-depth talks. Details can wait until you both match. Make every moment count, enjoy interesting conversations, and have a great time, no matter the outcome.</p>
    </div>
    <div class="code-card" style="left:679px">
      <svg viewBox="0 0 40 40"><path d="M14 26 5 17a5 5 0 0 1 9-6 5 5 0 0 1 9 6z" fill="#000"/><path d="M26 36 17 27a5 5 0 0 1 9-6 5 5 0 0 1 9 6z" fill="#000"/></svg>
      <h3>Casual<br>Dates</h3>
      <p>Our events are as easy as a casual chat. Unlike traditional speed dating or dating apps, we keep things light and fun. No formalities or pressure—just show up, find your date, and enjoy a relaxed conversation with someone new.</p>
    </div>
  </section>

  <section class="section faq">
    <h2>FAQs</h2>
    <ul class="faq-list">
      <li><span>What are the rules?</span><span>+</span></li>
      <li><span>What is your cancellation / no-show policy?</span><span>+</span></li>
      <li><span>How many dates will I go on?</span><span>+</span></li>
      <li><span>How long do I have on each date?</span><span>+</span></li>
      <li><span>What happens at the end of each date?</span><span>+</span></li>
      <li><span>I met someone I wanted to Match with, now what?</span><span>+</span></li>
      <li><span>Are there breaks in-between each date?</span><span>+</span></li>
      <li><span>I can’t seem to find my date. What should I do?</span><span>+</span></li>
      <li><span>What should I wear?</span><span>+</span></li>
      <li><span>How much do our events cost?</span><span>+</span></li>
      <li><span>Is Lantern partnered with their venues?</span><span>+</span></li>
      <li><span>Does Lantern keep any user information?</span><span>+</span></li>
    </ul>
  </section>

  <footer class="section footer">
    <div class="brand-name"><span class="dot"></span>Lantern Meetups</div>
    <h3>Contact</h3>
    <span class="line" style="top:153px">✉ hello@lanternmeetups.com</span>
    <span class="line" style="top:170px">☎ (555) 014-2290</span>
    <span class="line" style="top:216px">Copyright © 2023 Lantern Meetups. All Rights Reserved.</span>
  </footer>

</div>
</body>
</html>
```